NEW FACEBOOK AD CREATIVES FOR MARKETING AGENCY

We need one single static image AND a Carousel Ad Design With 5 Cards Total in it.

We advertise a SaaS Product that teaches businesses how to use incentive based marketing to get more sales and leads.

Using our service businesses can give away smart devices like smartwatches, earpods, mp4 players, tablets, etc. as a gift bonus along with their product or service as an added value benefit to help them create more attractive offers and to get more sales.

I have attached two designs that get me my best results on facebook ads so far so I want to create something very similar with a different look and showcasing 3-4 of the items I have attached images for.

CONTENT & INSTRUCTIONS:
MAIN TEXT: TRIPLE YOUR SALES OFFERING FREE SMART DEVICES AS A BONUS FOR BUYING YOUR PRODUCT OR SERVICE

Target Market(s)

ENTREPRENEURS, INVESTORS, BUSINESS OWNERS, MEDIA AGENCIES, BROKERAGES

Industry/Entity Type

marketing gifting

Requirements
Must have
• must match color scheme of website www.brightlooprewardhub.biz as this is where they will be redirected to when they click.
Nice to have
• the ads must be 1080x1080 Static newsfeed ad and carousel ads

```html
<!DOCTYPE html>
<html lang="en">
<head>
<meta charset="utf-8">
<title>Triple Your Sales – Ad Creative</title>
<link href="https://fonts.googleapis.com/css2?family=Anton&family=Roboto:wght@700&display=swap" rel="stylesheet">
<style>
  :root {
    --stage: #2f2f2f;
    --paper: #f5f5f5;
    --ink: #1e1e1e;
    --accent: #ff3a00;
    --ring: #1474c0;
    --button: #ffffff;
  }
  html, body {
    margin: 0;
    padding: 0;
    width: 1166px;
    height: 1200px;
    overflow: hidden;
    background: var(--stage);
  }
  .ad {
    position: absolute;
    left: 125px;
    top: 122px;
    width: 952px;
    height: 956px;
    background: var(--paper);
    overflow: hidden;
    font-family: "Anton", "Impact", sans-serif;
    color: var(--ink);
  }
  .art {
    position: absolute;
    inset: 0;
  }
  .headline {
    position: absolute;
    left: 0;
    right: 0;
    top: 78px;
    margin: 0;
    text-align: center;
    font-weight: 400;
    line-height: 1;
  }
  .headline span { display: block; }
  .headline .lead { font-size: 33px; }
  .headline .hero { font-size: 86px; color: var(--accent); margin-top: 2px; letter-spacing: 0.5px; }
  .headline .offer { font-size: 47px; margin-top: 2px; }
  .headline .detail { font-size: 35px; margin-top: 8px; line-height: 1.25; }
  .cta-band {
    position: absolute;
    left: 0;
    top: 855px;
    width: 952px;
    height: 101px;
    background: var(--accent);
  }
  .cta-button {
    position: absolute;
    left: 253px;
    top: 22px;
    width: 446px;
    height: 62px;
    background: var(--button);
    border-radius: 6px;
    box-shadow: 0 4px 10px rgba(0,0,0,0.25);
    display: flex;
    align-items: center;
    justify-content: center;
    font-family: "Roboto", "Arial", sans-serif;
    font-weight: 700;
    font-size: 29px;
    color: var(--accent);
    text-decoration: none;
  }
</style>
</head>
<body>
  <main class="ad">
    <svg class="art" width="952" height="956" viewBox="0 0 952 956" aria-hidden="false">
      <defs>
        <linearGradient id="card-airfare" x1="0" y1="0" x2="1" y2="1">
          <stop offset="0" stop-color="#f6a23a"/>
          <stop offset="0.55" stop-color="#f47a4c"/>
          <stop offset="1" stop-color="#b1489a"/>
        </linearGradient>
        <linearGradient id="card-dining" x1="0" y1="0" x2="1" y2="1">
          <stop offset="0" stop-color="#f0349a"/>
          <stop offset="0.6" stop-color="#d948b8"/>
          <stop offset="1" stop-color="#9b5ad8"/>
        </linearGradient>
        <linearGradient id="card-fitness" x1="0" y1="0" x2="1" y2="1">
          <stop offset="0" stop-color="#f7cf6a"/>
          <stop offset="0.6" stop-color="#f3b63a"/>
          <stop offset="1" stop-color="#e89a2a"/>
        </linearGradient>
        <linearGradient id="card-hotel" x1="0" y1="0" x2="1" y2="1">
          <stop offset="0" stop-color="#1f8f8f"/>
          <stop offset="0.6" stop-color="#3eb3b0"/>
          <stop offset="1" stop-color="#5fc9c4"/>
        </linearGradient>
        <filter id="card-shadow" x="-20%" y="-20%" width="140%" height="140%">
          <feDropShadow dx="0" dy="8" stdDeviation="10" flood-color="#000" flood-opacity="0.3"/>
        </filter>
      </defs>

      <g class="sparkles" stroke="var(--accent)" stroke-width="2.5">
        <path d="M142 380 h16 M150 372 v16"/>
        <path d="M768 327 h16 M776 319 v16"/>
      </g>
      <g stroke="#ffffff" stroke-width="3">
        <path d="M56 113 h18 M65 104 v18"/>
      </g>

      <path class="ring" d="M114 855 A362 362 0 0 1 838 855 L687 855 A211 211 0 0 0 265 855 Z" fill="var(--ring)"/>

      <g class="gift-cards" filter="url(#card-shadow)">
        <rect role="img" aria-label="Hotel savings gift card with resort photo" x="-98" y="-200" width="196" height="400" rx="12"
              transform="translate(721 615) rotate(10)" fill="url(#card-hotel)"/>
        <rect role="img" aria-label="Fitness gift card with workout photo" x="-98" y="-200" width="196" height="400" rx="12"
              transform="translate(564 600) rotate(3)" fill="url(#card-fitness)"/>
        <rect role="img" aria-label="Travel and dining gift card with restaurant photo" x="-98" y="-200" width="196" height="400" rx="12"
              transform="translate(396 585) rotate(-18)" fill="url(#card-dining)"/>
        <rect role="img" aria-label="Two roundtrip airfare gift card with airplane photo" x="-98" y="-200" width="196" height="400" rx="12"
              transform="translate(309 618) rotate(-30)" fill="url(#card-airfare)"/>
      </g>
    </svg>

    <h1 class="headline">
      <span class="lead">TRIPLE to</span>
      <span class="hero">3X YOUR SALES</span>
      <span class="offer">OFFERING FREE SMART DEVICES</span>
      <span class="detail">AS A BONUS FOR BUYING YOUR<br>PRODUCT OR SERVICE</span>
    </h1>

    <div class="cta-band">
      <a class="cta-button" href="https://www.brightlooprewardhub.biz">START A RISK FREE TRIAL</a>
    </div>
  </main>
</body>
</html>
```